Banner Design for High End Jewelry Website

We need a banner for our website (brindlestone.com) for a sale that we will be running. The banner should be a size 1187 × 400. I have included a few pieces of jewelry to be included in the banner (do not need to use all, can use just some). The banner should say:
"Christmas is Closer Than You Think Sale!"
Shop Now

Industry/Entity Type

Jewelry

```html
<!DOCTYPE html>
<html lang="en">
<head>
<meta charset="utf-8">
<title>Christmas Sale Banner</title>
<link rel="stylesheet" href="https://fonts.googleapis.com/css2?family=Arvo:wght@700&family=Merriweather:wght@700&family=Lobster&display=swap">
<style>
  :root {
    --frame-red: #e8313a;
    --headline-red: #ef4a4a;
    --button-red: #c8141c;
    --bg-light: #fbfbfb;
    --bg-mid: #ececee;
    --snow-tint: #dfe9f2;
    --gold: #c9a23a;
    --gold-deep: #9c7a1e;
  }
  html, body {
    margin: 0;
    padding: 0;
    width: 1200px;
    height: 404px;
    overflow: hidden;
    background: #ffffff;
  }
  .banner {
    position: relative;
    width: 1200px;
    height: 404px;
    box-sizing: border-box;
    border: 6px solid var(--frame-red);
    background: radial-gradient(ellipse at 60% 40%, var(--bg-light) 0%, var(--bg-mid) 100%);
    overflow: hidden;
  }
  .snow-pattern {
    position: absolute;
    inset: 0;
    background:
      radial-gradient(circle at 8% 70%, var(--snow-tint) 0, transparent 120px),
      radial-gradient(circle at 20% 30%, var(--snow-tint) 0, transparent 90px),
      radial-gradient(circle at 42% 78%, var(--snow-tint) 0, transparent 80px),
      radial-gradient(circle at 55% 20%, var(--snow-tint) 0, transparent 70px);
    opacity: 0.7;
  }
  .headline {
    position: absolute;
    left: 36px;
    top: 20px;
    margin: 0;
    white-space: nowrap;
    color: var(--headline-red);
    font-weight: 700;
  }
  .headline-lead {
    font-family: "Merriweather", Georgia, serif;
    font-size: 84px;
    letter-spacing: -1px;
  }
  .headline-rest {
    font-family: "Arvo", "Rockwell", serif;
    font-size: 38px;
    margin-left: 10px;
  }
  .shop-button {
    position: absolute;
    left: 104px;
    top: 216px;
    width: 308px;
    height: 95px;
    box-sizing: border-box;
    border: 5px solid var(--frame-red);
    border-radius: 6px;
    background: #ffffff;
    display: flex;
    align-items: center;
    justify-content: center;
    font-family: "Lobster", cursive;
    font-size: 50px;
    color: var(--button-red);
    text-decoration: none;
  }
  .jewelry-shadow {
    position: absolute;
    left: 620px;
    top: 340px;
    width: 540px;
    height: 34px;
    border-radius: 50%;
    background: radial-gradient(ellipse at center, rgba(0,0,0,0.3) 0%, rgba(0,0,0,0) 70%);
  }
  .jewelry-photo {
    position: absolute;
    left: 596px;
    top: 112px;
    width: 570px;
    height: 250px;
    border-radius: 40% 45% 45% 40%;
    background: radial-gradient(ellipse at 70% 55%, #e2bb4f 0%, var(--gold) 45%, var(--gold-deep) 80%, rgba(156,122,30,0) 100%);
  }
</style>
</head>
<body>
  <main class="banner">
    <div class="snow-pattern" role="img" aria-label="Soft pale blue snowflake pattern"></div>
    <h1 class="headline">
      <span class="headline-lead">Christmas</span><span class="headline-rest">is closer than you think sale!</span>
    </h1>
    <a class="shop-button" href="#">Shop Now!</a>
    <div class="jewelry-shadow"></div>
    <div class="jewelry-photo" role="img" aria-label="Gold cocktail ring with coloured cabochon stones and diamonds beside a gold scale-textured cuff bracelet set with pavé diamonds"></div>
  </main>
</body>
</html>
```